Zielgruppe
Branche: Logistik/Spedition
Spezifisch: Fahrzeugüberführung und weitere Dienstleistungen in der Branche siehe Webseite
Zielgruppe: Autohäuser, Leasinggesellschaften, Autovermietungen, Firmen mit eigenem Fuhrpark
Aufgabenstellung
Es handelt sich hierbei um ein Portfolio, welches als E-Mail Anhang an potentielle Kunden zugeschickt oder bei Anfragen per E-Mail mitgeschickt werden soll. Dieses Portfolio wünschen wir in Form einer PDF-Datei.
-Grafische, textliche und inhaltliche Orientierung an unserer Homepage
-alle Dienstleistungen sollen im Portfolio beschrieben werden
-Hauptdienstleistungen, die ausführlicher beschrieben werden sollen: Eigenachsüberfürhung (Hauptdienstleistung)

```html
<!DOCTYPE html>
<html lang="de">
<head>
<meta charset="utf-8">
<title>Relam Fleetservices – Portfolio</title>
<link href="https://fonts.googleapis.com/css2?family=Roboto:wght@300;400;500;700;900&display=swap" rel="stylesheet">
<style>
  :root{
    --blue:#2b9fe0;
    --blue-dark:#1d87c6;
    --ink:#1e1e1e;
    --text:#4a4a4a;
    --muted:#9a9a9a;
    --dark-tile:#3d3d3d;
    --page:#ffffff;
    --backdrop:#a8a8a8;
  }
  *{margin:0;padding:0;box-sizing:border-box}
  html,body{width:1200px;height:2942px;overflow:hidden}
  body{background:var(--backdrop);font-family:"Roboto",sans-serif;color:var(--ink);position:relative}
  .slide{position:absolute;left:215px;width:770px;height:433px;background:var(--page);overflow:hidden}
  .abs{position:absolute}
  .photo{position:absolute}
  .brand{position:absolute;font-family:"Roboto",sans-serif;font-weight:900;color:var(--blue);letter-spacing:1px;display:flex;align-items:center;gap:5px}
  .brand .dot{width:7px;height:7px;background:var(--blue)}
  .page-no{position:absolute;left:0;top:0;width:25px;height:25px;background:var(--blue);color:#fff;font-size:7px;display:flex;align-items:center;justify-content:center}
  .footer{position:absolute;left:30px;right:30px;bottom:20px;display:flex;align-items:center;gap:14px;font-size:5.5px;letter-spacing:1px;color:var(--muted);text-transform:uppercase}
  .footer .rule{flex:1;height:1px;background:#e3e3e3}
  .footer .url{text-transform:lowercase}

  /* Cover */
  .cover-band{position:absolute;left:0;top:155px;width:388px;height:125px;background:var(--blue);opacity:.93}
  .cover-frame{position:absolute;left:-10px;top:114px;width:399px;height:205px;border:3px solid #fff}
  .cover-title{position:absolute;left:46px;top:180px;color:#fff;font-weight:700;font-size:28px;line-height:34px}
  .cover-url{position:absolute;right:36px;bottom:20px;color:#fff;font-size:7px;letter-spacing:1px}

  /* Intro */
  .intro-title{position:absolute;left:0;width:100%;text-align:center;top:244px;font-size:18px;font-weight:500;color:var(--blue)}
  .intro-sub{position:absolute;left:0;width:100%;text-align:center;top:270px;font-size:18px;font-weight:500;color:var(--ink)}
  .intro-text{position:absolute;left:165px;width:440px;top:314px;text-align:center;font-size:9px;line-height:17px;color:var(--text)}

  /* About */
  .eyebrow{font-size:10px;font-weight:700;letter-spacing:2.5px;color:var(--ink)}
  .heading-blue{color:var(--blue);font-weight:500;font-size:25px;line-height:30px}
  .body-copy{font-size:8.5px;line-height:16px;color:var(--text);text-align:justify}
  .body-copy strong{color:var(--ink)}

  /* Features */
  .feature-heading{position:absolute;left:94px;top:96px;color:var(--blue);font-weight:500;font-size:20px;line-height:23px}
  .tile{position:absolute;width:146px;height:104px;display:flex;flex-direction:column;align-items:center;justify-content:center;gap:10px;font-size:8px;letter-spacing:2px;text-align:center;line-height:11px}
  .tile.dark{background:var(--dark-tile);color:#fff}
  .tile.blue{background:var(--blue);color:#fff}
  .tile.light{background:#fff;color:var(--ink)}
  .tile svg{width:34px;height:34px;fill:none;stroke:currentColor;stroke-width:1.6;stroke-linecap:round;stroke-linejoin:round}
  .tile.light svg{stroke:var(--blue)}

  /* Services */
  .svc{position:absolute;overflow:hidden}
  .svc .label{position:absolute;left:0;right:0;bottom:0;height:26px;background:linear-gradient(90deg,var(--blue) 55%,rgba(43,159,224,0));color:#fff;font-size:11px;font-weight:500;padding-left:16px;display:flex;align-items:center}
  .svc-text{position:absolute;left:193px;top:0;width:385px;height:218px;padding:24px 30px 0 30px;background:#fff}
</style>
</head>
<body>

<!-- Slide 1: Cover -->
<section class="slide" style="top:645px">
  <div class="photo" role="img" aria-label="Foto: Auto in voller Fahrt auf einer Autobahn bei Sonnenuntergang, Bewegungsunschärfe" style="inset:0;background:linear-gradient(180deg,#5a5f78 0%,#c99b88 28%,#9b8e9c 42%,#6f7a95 60%,#4d5677 100%)"></div>
  <div class="cover-band"></div>
  <div class="cover-frame"></div>
  <h1 class="cover-title">PROFESSIONELLE<br>AUTOÜBERFÜHRUNG</h1>
  <div class="brand" style="right:38px;top:36px;font-size:26px"><span class="dot"></span>RELAM</div>
  <div class="cover-url">www.yourdomain.com</div>
</section>

<!-- Slide 2: Intro -->
<section class="slide" style="top:1098px">
  <div class="photo" role="img" aria-label="Foto: Autobahn mit Autos vor Waldsilhouette im Abendlicht" style="left:0;top:0;width:770px;height:206px;background:linear-gradient(180deg,#4e5b73 0%,#b8a189 45%,#e0a866 62%,#3a3a36 80%,#6d6b67 100%)"></div>
  <h2 class="intro-title">Fahrzeugüberführung Mit Der Relam Gmbh –</h2>
  <p class="intro-sub">Autoüberführung Vom Profi</p>
  <p class="intro-text">Möchten Sie mehr über unsere Leistungen erfahren oder wünschen Sie ein unverbindliches Angebot für eine Fahrzeugüberführung? Dann stellen Sie jetzt Ihre Anfrage über unser branchenweit einmaliges Buchungsportal oder kontaktieren Sie uns persönlich – wir sind jederzeit gern für Sie da!</p>
  <div class="footer"><span>©2022 – Relam GmbH</span><span class="rule"></span><span class="url">www.yourdomain.com</span></div>
</section>

<!-- Slide 3: About -->
<section class="slide" style="top:1550px">
  <div class="page-no">3</div>
  <div class="brand" style="right:24px;top:20px;font-size:14px"><span class="dot" style="width:5px;height:5px"></span>RELAM</div>
  <div class="photo" role="img" aria-label="Foto: Lkw-Fahrer mit verschränkten Armen vor einem Lastwagen" style="left:59px;top:62px;width:217px;height:307px;background:linear-gradient(160deg,#dfe4ea 0%,#b9c2cc 45%,#7d6e68 70%,#8a3a3a 100%)"></div>
  <div class="abs" style="left:314px;top:60px;width:406px">
    <p class="eyebrow">FAHRZEUGÜBERFÜHRUNG:</p>
    <h2 class="heading-blue" style="margin-top:14px">Professionelle<br>Autoüberführung</h2>
    <p class="body-copy" style="margin-top:20px">Ist ein Fahrzeug von A nach B zu bringen und Ihnen fehlen die zeitlichen oder personellen Ressourcen dafür, benötigen Sie einen zuverlässigen Partner für die Autoüberführung. Ob im Auftrag von Leasing-Gesellschaften, Autovermietungen und Unternehmen mit eigener Fahrzeugflotte oder einzelnen Firmenwagen, aber auch für Privatkunden: Die RELAM GmbH überzeugt seit 2009 mit starken Leistungen im Bereich der Fahrzeugüberführung.</p>
    <p class="body-copy" style="margin-top:12px">Vom E-Fahrzeug über konventionelle Benziner bis hin zu ganzen Fuhrparks: Mit unserem Fokus auf Sicherheit, Pünktlichkeit und Transparenz bieten wir als Marktführer mit unserer Fahrzeugüberführung geprüfte Qualität, auf die Sie sich verlassen können – überzeugen Sie sich selbst!</p>
    <p class="body-copy" style="margin-top:12px"><strong>Zuverlässig ans Ziel mit einer Fahrzeugüberführung vom Experten: Profitieren Sie mit unserem europaweiten Service zur Autoüberführung auf Fremd- oder Eigenachse und von einer effektiven Distributionslösung!</strong></p>
  </div>
  <div class="footer"><span>©2022 – Relam GmbH</span><span class="rule"></span><span class="url">www.yourdomain.com</span></div>
</section>

<!-- Slide 4: Features -->
<section class="slide" style="top:2003px">
  <div class="page-no">4</div>
  <div class="brand" style="right:24px;top:20px;font-size:14px"><span class="dot" style="width:5px;height:5px"></span>RELAM</div>
  <h2 class="feature-heading">DAS<br>ZEICHNET<br>RELAM AUS</h2>
  <p class="body-copy abs" style="left:239px;top:96px;width:427px">Seit der Gründung im Jahre 2009 hat sich die R.E.L.A.M. GmbH als professioneller Dienstleister für Fahrzeugüberführungen etabliert. Unsere 200 geschulten und im gesamten Bundesgebiet ansässigen Fahrer ermöglichen es uns 20.000 Fahrzeuge pro Jahr sicher und zuverlässig zu überführen.</p>

  <div class="tile dark" style="left:239px;top:157px">
    <svg viewBox="0 0 34 34"><path d="M17 3 L29 8 V16 C29 24 23 29 17 31 C11 29 5 24 5 16 V8 Z"/><path d="M11 17 L15 21 L23 12"/></svg>
    <span>SICHERE<br>ÜBERFÜHRUNG</span>
  </div>
  <div class="tile light" style="left:385px;top:157px">
    <svg viewBox="0 0 34 34"><rect x="9" y="4" width="16" height="24"/><path d="M13 10h8M13 14h8M13 18h5"/><circle cx="22" cy="25" r="4"/></svg>
    <span style="color:var(--ink)">ZERTIFIZIERTE<br>QUALITÄT</span>
  </div>
  <div class="tile dark" style="left:531px;top:157px">
    <svg viewBox="0 0 34 34"><path d="M3 24 V12 H19 V24 M19 16 H26 L31 21 V24"/><circle cx="9" cy="26" r="3"/><circle cx="25" cy="26" r="3"/><path d="M12 26h10"/></svg>
    <span>SCHNELLE<br>BEARBEITUNG</span>
  </div>
  <div class="tile blue" style="left:94px;top:261px">
    <svg viewBox="0 0 34 34"><rect x="6" y="5" width="13" height="22" rx="2"/><rect x="16" y="9" width="13" height="20" rx="2"/><path d="M10 23h5M20 25h5"/></svg>
    <span>EIGENE APP</span>
  </div>
  <div class="tile light" style="left:239px;top:261px">
    <svg viewBox="0 0 34 34"><path d="M3 15 L10 11 L17 14 L24 11 L31 15"/><path d="M8 18 L14 24 C15 25 17 25 18 24 L26 17"/><path d="M12 16 L17 20"/></svg>
    <span style="color:var(--ink)">FAHRER<br>PROTOKOLL</span>
  </div>
  <div class="tile blue" style="left:385px;top:261px">
    <svg viewBox="0 0 34 34"><circle cx="17" cy="9" r="4"/><path d="M10 21 C10 16 24 16 24 21"/><path d="M5 24 H14 L20 27 L29 22"/></svg>
    <span>KUNDENPORTAL</span>
  </div>
  <div class="tile light" style="left:531px;top:261px">
    <svg viewBox="0 0 34 34"><circle cx="13" cy="17" r="9"/><circle cx="21" cy="17" r="9"/></svg>
    <span style="color:var(--ink)">TRANSPARENZ</span>
  </div>
  <div class="footer"><span>©2022 – Relam GmbH</span><span class="rule"></span><span class="url">www.yourdomain.com</span></div>
</section>

<!-- Slide 5: Services -->
<section class="slide" style="top:2455px">
  <div class="svc" style="left:0;top:0;width:193px;height:218px">
    <div class="photo" role="img" aria-label="Foto: Fahrzeug auf einem Autotransporter, Nahaufnahme des Reifens" style="inset:0;background:linear-gradient(160deg,#3f6f8a 0%,#1f2e3b 55%,#5e7b8c 100%)"></div>
    <div class="label">Fremdachsenüberführung</div>
  </div>
  <div class="svc-text">
    <p class="eyebrow" style="font-size:10px;letter-spacing:.5px">FAHRZEUGÜBERFÜHRUNG –</p>
    <h2 class="heading-blue" style="font-size:17px;line-height:23px;margin-top:2px">Unser Service Für Ihre<br>Autoüberführung</h2>
    <p class="body-copy" style="font-size:7.5px;line-height:15px;margin-top:12px;text-align:left">Die RELAM GmbH ist eines der führenden Unternehmen im Bereich Fahrzeugüberführung. Wir führen jährlich mehrere Zehntausend Eigenachsüberführungen durch, sowohl für private als auch für viele namhafte Kunden. Diese Position haben wir uns durch zuverlässigen und kundenorientierten Service erarbeitet. Fragen Sie direkt Ihre gewünschten Leistungen an und profitieren Sie von unserer Erfahrung und Expertise.</p>
  </div>
  <div class="svc" style="left:578px;top:0;width:192px;height:218px">
    <div class="photo" role="img" aria-label="Foto: beleuchtete Tiefgarage mit Stellplätzen" style="inset:0;background:linear-gradient(180deg,#4a5565 0%,#8a97a8 45%,#c4ccd6 70%,#6f7c8d 100%)"></div>
    <div class="label">Sichere Stellplätze</div>
  </div>
  <div class="svc" style="left:0;top:218px;width:385px;height:215px">
    <div class="photo" role="img" aria-label="Foto: Hand hält Smartphone mit Navigationskarte im Auto" style="inset:0;background:linear-gradient(120deg,#1d2a44 0%,#4c6384 40%,#b7a58c 70%,#2c3650 100%)"></div>
    <div class="label">Eigenachsenüberführung</div>
  </div>
  <div class="svc" style="left:385px;top:218px;width:193px;height:215px">
    <div class="photo" role="img" aria-label="Foto: Mitarbeiter poliert ein Auto mit einem Mikrofasertuch" style="inset:0;background:linear-gradient(150deg,#c8cdd2 0%,#8c8e8f 45%,#d1b04a 65%,#4f5a66 100%)"></div>
    <div class="label">Fahrzeugaufbereitung</div>
  </div>
  <div class="svc" style="left:578px;top:218px;width:192px;height:215px">
    <div class="photo" role="img" aria-label="Foto: Reifenwechsel mit Druckmessgerät an einer Felge" style="inset:0;background:linear-gradient(160deg,#6d7f95 0%,#2d3d57 50%,#8d9bb0 100%)"></div>
    <div class="label">Reifenhandling</div>
  </div>
</section>

</body>
</html>
```